Our company needs a Corporate Identity Package!!!

We would like to receive submissions for a corporate identity pachage including the following elements:

1. Presentation Folder
2. Product/Service Catalogue (16 A4 pages landscape but expandable)
3. Product Brochure (up to 8 A4 pages)
4. Product Flyer (2 A4 pages)
5. Business Card
6. Letterhead
7. Envelope
8. E-mail signature.

I attach a Presentation Folder that i like (geometric but also has circle). We would like to have some ideas regarding the above 7 elements including vantrime logo colors (vantrime.example).

Payment is indicative and we are planning to increase the payment now that we found out how to actually do this. You are also more than welcome to send us a message and suggest the amount of payment for your Corporate Identity elements and we will update this.

Target Market(s)

Home | Office | Life

Colors
f78f20
0555a3
9bcb3b

Requirements
Must have
• 1. Presentation Folder
• 2. Product/Service Catalogue (16 A4 pages landscape but to be easily expandable)
• 3. Product Brochure (up to 4 A4 pages but to be easily expandable )
• 4. Product Flyer (2 A4 pages)
• 5. Business Card
• 6. Letterhead
• 7. Envelope
• 8. E-mail signature.
Nice to have
• It would be nice to include design something around the cycle that communicates the best six doctors (i.e. sunshine, water, rest, air, exercise and diet) !!!

```html
<!DOCTYPE html>
<html lang="en">
<head>
<meta charset="utf-8">
<title>vantrime — Corporate Identity Package</title>
<link href="https://fonts.googleapis.com/css2?family=Open+Sans:wght@400;600;700&display=swap" rel="stylesheet">
<style>
:root{
  --navy:#1b2547;
  --navy-soft:#2e3550;
  --blue:#0555a3;
  --orange:#f78f20;
  --green:#9bcb3b;
  --white:#ffffff;
  --paper:#f4f4f4;
  --ink:#333a48;
  --rule:#b9bec8;
  --number:#3d4a5c;
}
*{box-sizing:border-box;margin:0;padding:0}
html,body{width:1200px;height:604px;overflow:hidden;background:#cfcfcf}
body{font-family:"Open Sans",Arial,sans-serif;color:var(--ink)}
.canvas{position:relative;width:1200px;height:604px;overflow:hidden}
.abs{position:absolute}

/* staging backgrounds */
.bg-folder{left:0;top:0;width:243px;height:226px;background:#d9d9d9}
.bg-cards{left:243px;top:0;width:314px;height:226px;background:#e9ecef}
.bg-letter{left:557px;top:0;width:285px;height:234px;background:#efefef}
.bg-flyer{left:842px;top:0;width:358px;height:234px;background:#1d1d1d}
.bg-catalogue{left:0;top:226px;width:162px;height:378px;background:#d4d4d4}
.bg-brochure{left:162px;top:226px;width:483px;height:378px;background:#7b7b7b}
.bg-envelope{left:645px;top:234px;width:555px;height:370px;background:#262626}

.item-no{position:absolute;font-weight:700;font-size:24px;color:var(--number);line-height:1}
.item-no.on-dark{color:#4a5673}
.item-no.light{color:#ffffff}

/* shared brand pieces */
.pattern{position:absolute;
  background:linear-gradient(135deg,var(--orange) 0%,var(--green) 45%,var(--blue) 100%);
  clip-path:polygon(28% 0,100% 8%,92% 58%,62% 100%,34% 82%,0 66%,8% 28%)}
.logo{position:absolute;display:flex;align-items:center;gap:4px}
.logo-dot{border-radius:50%;background:var(--orange);flex:none}
.logo-name{font-weight:700;letter-spacing:.2px;line-height:1;white-space:nowrap}
.on-dark .logo-name{color:var(--white)}
.on-light .logo-name{color:var(--blue)}
.tagline{position:absolute;font-size:5px;font-weight:600;letter-spacing:.8px;color:#9fb2d6;white-space:nowrap}
.fine{font-size:4.5px;line-height:6px;color:#555}
.text-bar{height:2px;background:var(--rule);margin-bottom:2px;border-radius:1px}
.photo{position:absolute;background:linear-gradient(160deg,#d9c8b8,#9c8a7d)}
.shadow{box-shadow:0 2px 6px rgba(0,0,0,.25)}

/* 1 folder */
.folder-pocket{left:176px;top:38px;width:34px;height:174px;background:var(--green)}
.folder-cover{left:26px;top:14px;width:160px;height:198px;background:var(--navy);overflow:hidden}

/* 5 business cards */
.card{width:140px;height:82px;overflow:hidden}
.card-front{left:262px;top:22px;background:var(--white)}
.card-back{left:388px;top:118px;background:var(--navy)}

/* 6 letterhead */
.letter-sheet{left:622px;top:12px;width:150px;height:206px;background:var(--white);overflow:hidden}
.letter-footer{position:absolute;left:0;bottom:0;width:100%;height:12px;background:var(--navy);
  display:flex;gap:8px;align-items:center;padding:0 6px;font-size:4.5px;color:#dfe4f0;white-space:nowrap}
.ring{position:absolute;border-radius:50%;background:var(--white);border:3px solid var(--orange)}

/* 4 flyer */
.flyer-page{top:18px;width:150px;height:200px;background:var(--white);overflow:hidden}
.flyer-front{left:852px}
.flyer-back{left:1016px}
.flyer-navy{left:0;top:0;width:100%;height:100%;background:var(--blue);
  clip-path:polygon(0 24%,80% 16%,80% 58%,0 88%)}
.flyer-arc{left:44px;top:38px;width:160px;height:160px;border-radius:50%;background:var(--orange)}
.flyer-title{font-size:8px;font-weight:700;color:var(--orange);letter-spacing:.4px;white-space:nowrap}
.flyer-footer{position:absolute;left:6px;right:6px;bottom:4px;display:flex;gap:6px;font-size:4.5px;line-height:6px;color:var(--white);white-space:nowrap;z-index:2}

/* 2 catalogue thumbnails */
.thumb{position:absolute;width:68px;height:46px;background:var(--white);overflow:hidden}
.thumb-title{position:absolute;left:6px;top:6px;font-size:4px;font-weight:700;color:var(--orange);white-space:nowrap}
.thumb-title.white{color:var(--white)}
.dot{position:absolute;border-radius:50%}

/* 3 brochure */
.page{position:absolute;width:86px;height:112px;overflow:hidden;background:var(--navy)}
.page.white{background:var(--white)}
.page-title{position:absolute;left:8px;top:10px;font-size:6px;font-weight:700;color:var(--white);white-space:nowrap;z-index:2}
.page-title.green{color:var(--green)}
.page-title.orange{color:var(--orange)}
.page-copy{position:absolute;left:8px;right:8px;font-size:4.5px;line-height:6px;color:#c9cfdd}
.page.white .page-copy{color:#555}
.page-logo{position:absolute;right:6px;bottom:5px;font-size:4px;font-weight:700;color:var(--blue)}
.page .page-logo.light{color:var(--white)}

/* elements list */
.elements{left:491px;top:245px;width:207px;height:185px;background:var(--navy-soft);
  padding:30px 18px 0 22px;color:var(--white);font-size:9px;font-weight:600;line-height:13.5px;list-style:none}

/* 7 envelope */
.envelope-back{left:705px;top:262px;width:210px;height:118px;background:#f1f1f1;overflow:hidden}
.envelope-flap{position:absolute;left:0;top:0;width:100%;height:18px;background:var(--navy)}
.envelope-front{left:875px;top:358px;width:300px;height:168px;background:#f6f6f6;overflow:hidden}
.envelope-address{position:absolute;right:14px;bottom:10px;text-align:right;font-size:5px;line-height:7px;color:var(--navy)}

/* 8 email signature */
.signature{left:618px;top:501px;width:241px;height:99px;background:var(--white);display:flex;align-items:center;padding:0 10px}
.sig-mark{width:46px;height:46px;border-radius:50%;background:var(--blue);border:5px solid var(--orange);flex:none}
.sig-rule{width:2px;height:62px;background:var(--blue);margin:0 8px 0 22px;flex:none}
.sig-body{font-size:5px;line-height:8px;color:#333}
.sig-name{font-size:8px;font-weight:700;color:var(--blue)}
.sig-markets{font-size:5px;font-weight:600;color:#333;margin-left:6px}
.sig-link{color:var(--orange)}
.sig-social{display:flex;gap:3px;margin-top:3px}
.sig-social span{width:6px;height:6px;border-radius:50%;border:1px solid var(--blue)}
</style>
</head>
<body>
<main class="canvas">

  <!-- staging backgrounds -->
  <div class="abs bg-folder"></div>
  <div class="abs bg-cards"></div>
  <div class="abs bg-letter"></div>
  <div class="abs bg-flyer"></div>
  <div class="abs bg-catalogue"></div>
  <div class="abs bg-brochure"></div>
  <div class="abs bg-envelope"></div>

  <!-- 1 presentation folder -->
  <section class="folder" aria-label="Presentation folder">
    <div class="abs folder-pocket"></div>
    <div class="abs folder-cover on-dark">
      <div class="pattern" style="left:92px;top:0;width:68px;height:58px" role="img" aria-label="Geometric cube pattern in orange, green and blue"></div>
      <div class="logo" style="left:36px;top:88px"><span class="logo-dot" style="width:14px;height:14px"></span><span class="logo-name" style="font-size:17px">vantrime</span></div>
      <div class="tagline" style="left:58px;top:108px">HOME | OFFICE | LIFE</div>
    </div>
    <span class="item-no" style="left:214px;top:164px">1</span>
  </section>

  <!-- 5 business cards -->
  <section aria-label="Business card">
    <div class="abs card card-front shadow on-light">
      <div class="logo" style="left:10px;top:12px"><span class="logo-dot" style="width:9px;height:9px"></span><span class="logo-name" style="font-size:11px">vantrime</span></div>
      <div class="abs fine" style="left:12px;top:38px">101 Harbor Lane, Eastbrook<br>+1 555 014 2290<br>hello@vantrime.example<br>www.vantrime.example</div>
      <div class="pattern" style="left:92px;top:6px;width:48px;height:66px" role="img" aria-label="Geometric cube pattern"></div>
    </div>
    <div class="abs card card-back shadow on-dark">
      <div class="pattern" style="left:0;top:30px;width:42px;height:52px" role="img" aria-label="Geometric cube pattern"></div>
      <div class="logo" style="left:48px;top:30px"><span class="logo-dot" style="width:10px;height:10px"></span><span class="logo-name" style="font-size:13px">vantrime</span></div>
      <div class="tagline" style="left:66px;top:46px;font-size:4px">HOME | OFFICE | LIFE</div>
    </div>
    <span class="item-no" style="left:538px;top:148px">5</span>
  </section>

  <!-- 6 letterhead -->
  <section aria-label="Letterhead">
    <div class="abs letter-sheet shadow on-light">
      <div class="logo" style="left:8px;top:12px"><span class="logo-dot" style="width:7px;height:7px"></span><span class="logo-name" style="font-size:8px">vantrime</span></div>
      <div class="pattern" style="left:104px;top:142px;width:46px;height:50px" role="img" aria-label="Geometric cube pattern"></div>
      <div class="ring" style="left:92px;top:174px;width:18px;height:18px"></div>
      <div class="letter-footer"><span>+1 555 014 2290</span><span>hello@vantrime.example</span><span>Harbor Lane</span></div>
    </div>
    <span class="item-no" style="left:813px;top:124px">6</span>
  </section>

  <!-- 4 product flyer -->
  <section aria-label="Product flyer">
    <div class="abs flyer-page flyer-front on-dark">
      <div class="abs flyer-navy"></div>
      <div class="abs flyer-arc"></div>
      <div class="pattern" style="left:104px;top:0;width:46px;height:38px" role="img" aria-label="Geometric cube pattern"></div>
      <div class="logo" style="left:44px;top:60px"><span class="logo-dot" style="width:10px;height:10px"></span><span class="logo-name" style="font-size:12px">vantrime</span></div>
      <div class="ring" style="left:88px;top:122px;width:30px;height:30px;border-color:var(--blue)"></div>
      <div class="pattern" style="left:6px;top:132px;width:38px;height:38px" role="img" aria-label="Geometric cube pattern"></div>
      <div class="flyer-footer"><span>hello@vantrime.example</span><span>+1 555 014 2290</span></div>
    </div>
    <div class="abs flyer-page flyer-back">
      <div class="pattern" style="left:104px;top:0;width:46px;height:38px" role="img" aria-label="Geometric cube pattern"></div>
      <div class="abs flyer-title" style="left:10px;top:22px">OUR PRODUCTS</div>
      <svg class="abs" style="left:12px;top:42px" width="120" height="34" viewBox="0 0 120 34" aria-hidden="true">
        <g fill="none" stroke="#f78f20" stroke-width="1.4">
          <polygon points="10,2 28,2 37,17 28,32 10,32 1,17"/>
          <polygon points="50,2 68,2 77,17 68,32 50,32 41,17"/>
          <polygon points="90,2 108,2 117,17 108,32 90,32 81,17"/>
        </g>
      </svg>
      <div class="abs" style="left:10px;top:80px;width:126px;display:flex;justify-content:space-between;font-size:4.5px;font-weight:700;color:var(--orange);white-space:nowrap"><span>Health products</span><span>Health products</span><span>Health products</span></div>
      <div class="abs fine" style="left:10px;top:96px;width:130px">Simple goods for home, office and daily life.</div>
      <div class="abs" style="left:10px;top:108px;width:130px">
        <div class="text-bar"></div><div class="text-bar"></div><div class="text-bar"></div><div class="text-bar" style="width:70%"></div>
      </div>
      <div class="pattern" style="left:104px;top:154px;width:46px;height:44px" role="img" aria-label="Geometric cube pattern"></div>
    </div>
    <span class="item-no on-dark" style="left:1174px;top:170px">4</span>
  </section>

  <!-- 2 product / service catalogue -->
  <section aria-label="Product and service catalogue">
    <div class="thumb" style="left:8px;top:232px"><div class="pattern" style="left:0;top:0;width:28px;height:26px" role="img" aria-label="Geometric cube pattern"></div><div class="ring" style="left:28px;top:14px;width:18px;height:18px;border-color:var(--blue)"></div></div>
    <div class="thumb" style="left:82px;top:232px;background:var(--blue)"><span class="thumb-title white" style="top:20px">Lorem ipsum</span><div class="pattern" style="left:48px;top:0;width:20px;height:30px" role="img" aria-label="Geometric cube pattern"></div></div>

    <div class="thumb" style="left:8px;top:284px"><div class="dot" style="left:4px;top:6px;width:34px;height:34px;border:2px solid var(--blue)"></div><span class="thumb-title" style="left:40px">Lorem ipsum</span></div>
    <div class="thumb" style="left:82px;top:284px;background:var(--orange)"><span class="thumb-title white" style="top:20px">Lorem ipsum</span></div>

    <div class="thumb" style="left:8px;top:336px"><div class="dot" style="left:6px;top:14px;width:16px;height:16px;border:2px solid var(--blue)"></div><div class="dot" style="left:26px;top:14px;width:16px;height:16px;border:2px solid #e5d21c"></div><div class="dot" style="left:46px;top:14px;width:16px;height:16px;border:2px solid var(--orange)"></div></div>
    <div class="thumb" style="left:82px;top:336px;display:grid;grid-template-columns:1fr 1fr 1fr;grid-template-rows:1fr 1fr">
      <div style="background:var(--green)"></div><div style="background:var(--blue)"></div><div style="background:var(--orange)"></div>
      <div style="background:var(--green)"></div><div style="background:var(--navy)"></div><div style="background:var(--orange)"></div>
    </div>

    <div class="thumb" style="left:8px;top:388px"><span class="thumb-title">Lorem ipsum</span><div class="abs" style="left:10px;top:16px;width:30px"><div class="text-bar" style="background:#333"></div><div class="text-bar" style="background:#333"></div><div class="text-bar" style="background:#333"></div><div class="text-bar" style="background:#333"></div></div></div>
    <div class="thumb" style="left:82px;top:388px"><span class="thumb-title">Lorem ipsum</span><div class="photo" style="left:36px;top:0;width:32px;height:46px" role="img" aria-label="Photo of a woman exercising"></div></div>

    <div class="thumb" style="left:8px;top:440px;background:#cddc2a"><span class="thumb-title white" style="top:20px">Lorem ipsum</span></div>
    <div class="thumb" style="left:82px;top:440px"><span class="thumb-title">Lorem ipsum</span><div class="dot" style="left:22px;top:18px;width:10px;height:10px;background:#6ec3e6"></div><div class="dot" style="left:42px;top:18px;width:10px;height:10px;background:#6ec3e6"></div></div>

    <div class="thumb" style="left:8px;top:492px"><div class="dot" style="left:30px;top:6px;width:34px;height:34px;background:#cddc2a"></div><div class="dot" style="left:20px;top:4px;width:12px;height:12px;background:var(--orange)"></div></div>
    <div class="thumb" style="left:82px;top:492px"><div class="photo" style="left:0;top:0;width:40px;height:46px;background:linear-gradient(160deg,#cfd8e3,#8a97a8)" role="img" aria-label="Photo of a fitness group"></div><span class="thumb-title" style="left:42px;font-size:3.5px">Lorem ipsum</span></div>

    <div class="thumb" style="left:8px;top:544px"><span class="thumb-title">Lorem ipsum</span><div class="abs" style="left:20px;top:16px;width:40px"><div class="text-bar"></div><div class="text-bar"></div><div class="text-bar"></div></div></div>
    <div class="thumb" style="left:82px;top:544px;background:var(--navy)"><div class="pattern" style="left:48px;top:0;width:20px;height:34px" role="img" aria-label="Geometric cube pattern"></div><div class="ring" style="left:52px;top:30px;width:12px;height:12px"></div></div>

    <span class="item-no" style="left:150px;top:320px">2</span>
  </section>

  <!-- 3 product brochure -->
  <section aria-label="Product brochure">
    <div class="page on-dark" style="left:187px;top:236px">
      <div class="pattern" style="left:50px;top:0;width:36px;height:30px" role="img" aria-label="Geometric cube pattern"></div>
      <div class="logo" style="left:12px;top:46px"><span class="logo-dot" style="width:9px;height:9px"></span><span class="logo-name" style="font-size:11px">vantrime</span></div>
      <div class="abs" style="left:12px;top:64px;font-size:6px;font-weight:700;color:var(--white);white-space:nowrap">Product Brochure</div>
    </div>
    <div class="page" style="left:277px;top:236px">
      <div class="page-title" style="left:24px;top:16px">Our products</div>
      <div class="page-copy" style="top:30px">Clean design, useful products and honest service for every room.</div>
      <div class="abs" style="left:8px;top:52px;width:70px"><div class="text-bar" style="background:#5a6382"></div><div class="text-bar" style="background:#5a6382"></div><div class="text-bar" style="background:#5a6382"></div><div class="text-bar" style="background:#5a6382"></div><div class="text-bar" style="background:#5a6382"></div></div>
      <span class="page-logo light">vantrime</span>
    </div>
    <div class="page" style="left:367px;top:236px">
      <div class="page-title">Our products</div>
      <svg class="abs" style="left:6px;top:28px" width="74" height="74" viewBox="0 0 74 74" aria-hidden="true">
        <g fill="none" stroke-width="1.2">
          <polygon stroke="#f78f20" points="7,2 17,2 22,11 17,20 7,20 2,11"/>
          <polygon stroke="#f78f20" points="32,2 42,2 47,11 42,20 32,20 27,11"/>
          <polygon stroke="#f78f20" points="57,2 67,2 72,11 67,20 57,20 52,11"/>
          <polygon stroke="#f78f20" points="7,27 17,27 22,36 17,45 7,45 2,36"/>
          <polygon stroke="#f78f20" points="32,27 42,27 47,36 42,45 32,45 27,36"/>
          <polygon stroke="#f78f20" points="57,27 67,27 72,36 67,45 57,45 52,36"/>
          <polygon stroke="#0555a3" points="7,52 17,52 22,61 17,70 7,70 2,61"/>
          <polygon stroke="#0555a3" points="32,52 42,52 47,61 42,70 32,70 27,61"/>
          <polygon stroke="#0555a3" points="57,52 67,52 72,61 67,70 57,70 52,61"/>
        </g>
      </svg>
      <span class="page-logo light">vantrime</span>
    </div>

    <div class="page white" style="left:187px;top:350px">
      <div class="page-title green">Health products</div>
      <svg class="abs" style="left:6px;top:40px" width="74" height="22" viewBox="0 0 74 22" aria-hidden="true">
        <g fill="none" stroke="#f78f20" stroke-width="1.2">
          <polygon points="7,2 17,2 22,11 17,20 7,20 2,11"/>
          <polygon points="32,2 42,2 47,11 42,20 32,20 27,11"/>
          <polygon points="57,2 67,2 72,11 67,20 57,20 52,11"/>
        </g>
      </svg>
      <div class="pattern" style="left:58px;top:68px;width:28px;height:30px" role="img" aria-label="Geometric cube pattern"></div>
      <div class="abs" style="left:8px;top:72px;width:46px"><div class="text-bar"></div><div class="text-bar"></div><div class="text-bar"></div></div>
    </div>
    <div class="page white" style="left:277px;top:350px">
      <div class="page-copy" style="top:10px">Made to last, built for everyday comfort.</div>
      <div class="photo" style="left:52px;top:28px;width:28px;height:22px" role="img" aria-label="Photo of a living room"></div>
      <div class="photo" style="left:8px;top:58px;width:30px;height:24px" role="img" aria-label="Photo of a home interior"></div>
      <div class="abs" style="left:44px;top:60px;width:36px"><div class="text-bar"></div><div class="text-bar"></div><div class="text-bar"></div></div>
      <span class="page-logo">vantrime</span>
    </div>
    <div class="page white" style="left:367px;top:350px">
      <div class="page-title orange">Health products</div>
      <div class="photo" style="left:8px;top:22px;width:34px;height:28px" role="img" aria-label="Photo of people in a fitness class"></div>
      <div class="page-copy" style="top:56px">Fresh ideas for a healthy home.</div>
      <div class="abs" style="left:8px;top:72px;width:70px"><div class="text-bar"></div><div class="text-bar"></div><div class="text-bar"></div></div>
      <span class="page-logo">vantrime</span>
    </div>

    <div class="page" style="left:187px;top:466px">
      <div class="page-title green">Health products</div>
      <div class="page-copy" style="top:22px">Move more and feel better every day.</div>
      <div class="photo" style="left:42px;top:50px;width:38px;height:44px" role="img" aria-label="Photo of a woman with a dumbbell"></div>
      <span class="page-logo light">vantrime</span>
    </div>
    <div class="page" style="left:277px;top:466px">
      <svg class="abs" style="left:10px;top:10px" width="66" height="92" viewBox="0 0 66 92" aria-hidden="true">
        <g fill="none" stroke-width="1.2">
          <polygon stroke="#9bcb3b" points="8,2 20,2 26,13 20,24 8,24 2,13"/>
          <polygon stroke="#9bcb3b" points="40,20 52,20 58,31 52,42 40,42 34,31"/>
          <polygon stroke="#f78f20" points="8,38 20,38 26,49 20,60 8,60 2,49"/>
          <polygon stroke="#0555a3" points="40,56 52,56 58,67 52,78 40,78 34,67"/>
          <polygon stroke="#0555a3" points="8,68 20,68 26,79 20,90 8,90 2,79"/>
        </g>
      </svg>
      <span class="page-logo light">vantrime</span>
    </div>
    <div class="page" style="left:367px;top:466px">
      <div class="dot" style="left:8px;top:28px;width:34px;height:34px;background:var(--orange)"></div>
      <div class="dot" style="left:46px;top:30px;width:14px;height:14px;background:var(--green)"></div>
      <div class="dot" style="left:62px;top:48px;width:14px;height:14px;background:var(--orange)"></div>
      <div class="dot" style="left:10px;top:70px;width:12px;height:12px;background:var(--green)"></div>
      <div class="dot" style="left:30px;top:70px;width:18px;height:18px;background:var(--blue)"></div>
      <div class="dot" style="left:54px;top:70px;width:14px;height:14px;background:var(--green)"></div>
      <span class="page-logo light">vantrime</span>
    </div>
    <div class="page" style="left:512px;top:466px">
      <div class="pattern" style="left:34px;top:10px;width:52px;height:60px" role="img" aria-label="Geometric cube pattern"></div>
      <div class="ring" style="left:34px;top:42px;width:22px;height:22px"></div>
      <span class="page-logo light">vantrime</span>
    </div>

    <div class="pattern" style="left:164px;top:318px;width:22px;height:28px" role="img" aria-label="Geometric cube pattern"></div>
    <div class="pattern" style="left:448px;top:470px;width:40px;height:56px" role="img" aria-label="Geometric cube pattern"></div>
    <div class="pattern" style="left:168px;top:532px;width:32px;height:48px" role="img" aria-label="Geometric cube pattern"></div>
    <span class="item-no light" style="left:468px;top:256px">3</span>
  </section>

  <!-- elements list -->
  <ol class="abs elements" aria-label="Identity elements">
    <li>1. Presentation Folder</li>
    <li>2. Product/Service Catalogue (16 A4 pages landscape but expandable)</li>
    <li>3. Product Brochure (up to 8 A4 pages)</li>
    <li>4. Product Flyer (2 A4 pages)</li>
    <li>5. Business Card</li>
    <li>6. Letterhead</li>
    <li>7. Envelope</li>
    <li>8. E-mail signature.</li>
  </ol>

  <!-- 7 envelope -->
  <section aria-label="Envelope">
    <div class="abs envelope-back"><div class="envelope-flap"></div></div>
    <div class="abs envelope-front on-light">
      <div class="pattern" style="left:200px;top:6px;width:84px;height:64px" role="img" aria-label="Geometric cube pattern"></div>
      <div class="logo" style="left:90px;top:92px"><span class="logo-dot" style="width:12px;height:12px"></span><span class="logo-name" style="font-size:16px">vantrime</span></div>
      <div class="envelope-address">101 Harbor Lane, Eastbrook<br>+1 555 014 2290<br>hello@vantrime.example</div>
    </div>
    <span class="item-no light" style="left:1155px;top:296px">7</span>
  </section>

  <!-- 8 email signature -->
  <section class="abs signature" aria-label="E-mail signature">
    <div class="sig-mark"></div>
    <div class="sig-rule"></div>
    <div class="sig-body">
      <div><span class="sig-name">vantrime</span><span class="sig-markets">Home | Office | Life</span></div>
      <div>418 Harbor Lane, Suite 12, Eastbrook,<br>Northfield 55120</div>
      <div>t +1 (555) 014 - 2290 &nbsp;|&nbsp; m 0155 - 010 - 447</div>
      <div><span class="sig-link">mail:</span> hello@vantrime.example &nbsp;|&nbsp; <span class="sig-link">website:</span> www.vantrime.example</div>
      <div class="sig-social" aria-label="Social links"><span></span><span></span><span></span><span></span></div>
    </div>
    <span class="item-no" style="left:218px;top:15px">8</span>
  </section>

</main>
</body>
</html>
```